Brindle's Business Card

I need some designs for a new business card including the new logo attached. An old example of our business card is also attached to show all the data that should be included on the new design.
**I added some more examples someone had mocked up**

Contact Information for Business Card

Should include all info on other examples uploaded.

```html
<!DOCTYPE html>
<html lang="en">
<head>
<meta charset="utf-8">
<title>Brindle's Business Card</title>
<link href="https://fonts.googleapis.com/css2?family=Montserrat:wght@300;400;500;600;800&display=swap" rel="stylesheet">
<style>
  :root {
    --backdrop: #e4e3e1;
    --navy: #02305c;
    --navy-light: #064a7c;
    --red: #d71a21;
    --blue: #0b6db5;
    --white: #ffffff;
    --card-white: #f1f1f1;
    --text-blue: #0b5fa5;
  }
  * { margin: 0; padding: 0; box-sizing: border-box; }
  html, body {
    width: 1200px; height: 1200px; overflow: hidden;
    background: var(--backdrop);
    font-family: "Montserrat", sans-serif;
  }
  .card {
    position: absolute;
    left: 235px;
    width: 730px;
    height: 418px;
    overflow: hidden;
  }
  .card-front {
    top: 160px;
    background: linear-gradient(200deg, var(--navy-light) 0%, var(--navy) 55%, #012a52 100%);
    color: var(--white);
  }
  .card-back {
    top: 631px;
    background: linear-gradient(160deg, #f7f7f7 0%, var(--card-white) 60%, #e6e6e6 100%);
  }
  .accent { color: var(--red); }

  .service-area, .call-to-action {
    position: absolute;
    left: 237px;
    font-size: 16.5px;
    font-weight: 600;
    line-height: 23px;
    letter-spacing: 0.2px;
  }
  .service-area { top: 62px; }
  .call-to-action { top: 312px; }

  .brand-mark {
    position: absolute;
    left: 104px;
    top: 168px;
    width: 86px;
    height: 86px;
    border-radius: 50%;
    background: var(--red);
  }
  .brand-name {
    position: absolute;
    left: 232px;
    top: 162px;
    font-size: 66px;
    font-weight: 500;
    line-height: 80px;
    letter-spacing: -0.5px;
    color: var(--white);
  }
  .brand-tagline {
    position: absolute;
    left: 237px;
    top: 235px;
    font-size: 18.3px;
    font-weight: 600;
    color: var(--red);
    letter-spacing: 0.1px;
  }

  .bands { position: absolute; inset: 0; }
  .band-label {
    position: absolute;
    font-size: 22px;
    font-weight: 400;
    color: var(--white);
    letter-spacing: 0.3px;
  }
  .band-label.top { left: 71px; top: 12px; }
  .band-label.bottom { left: 301px; top: 379px; }

  .person-name {
    position: absolute;
    left: 71px;
    top: 112px;
    font-size: 31px;
    font-weight: 800;
    color: var(--red);
    letter-spacing: -0.3px;
  }
  .name-rule {
    position: absolute;
    left: 71px;
    top: 161px;
    width: 111px;
    height: 3px;
    background: var(--blue);
  }
  .contact-list {
    position: absolute;
    left: 71px;
    top: 246px;
    list-style: none;
  }
  .contact-item {
    display: flex;
    align-items: center;
    gap: 8px;
    font-size: 22px;
    font-weight: 400;
    color: var(--text-blue);
    height: 32px;
  }
  .contact-item svg { width: 18px; height: 18px; flex: none; }

  .back-brand {
    position: absolute;
    left: 490px;
    top: 140px;
    width: 170px;
    display: flex;
    flex-direction: column;
    align-items: center;
    gap: 14px;
  }
  .back-brand .brand-dot {
    width: 90px; height: 90px; border-radius: 50%;
    background: var(--blue);
  }
  .back-brand .brand-word {
    font-size: 28px;
    font-weight: 600;
    color: var(--red);
  }
</style>
</head>
<body>

<section class="card card-front">
  <p class="service-area">SERVES CEDAR BEND, IA &amp;<br><span class="accent">SURROUNDING AREAS</span></p>
  <div class="brand-mark" aria-hidden="true"></div>
  <h1 class="brand-name">BRINDLE'S</h1>
  <p class="brand-tagline">AIR CONDITIONING &amp; HEATING SERVICE</p>
  <p class="call-to-action">CALL TODAY FOR ALL YOUR <span class="accent">HVAC</span>,<br><span class="accent">REFRIGERATION</span> &amp; <span class="accent">PLUMBING NEEDS</span></p>
</section>

<section class="card card-back">
  <svg class="bands" viewBox="0 0 730 418" width="730" height="418" aria-hidden="true">
    <polygon points="0,0 420,0 372,50 0,50" fill="var(--red)"/>
    <polygon points="436,0 730,0 730,50 388,50" fill="var(--blue)"/>
    <polygon points="0,367 200,367 250,417 0,417" fill="var(--red)"/>
    <polygon points="216,367 730,367 730,417 266,417" fill="var(--blue)"/>
  </svg>
  <p class="band-label top">LICENSED &amp; INSURED</p>

  <h2 class="person-name">DALE BRINDLE</h2>
  <div class="name-rule"></div>

  <ul class="contact-list">
    <li class="contact-item">
      <svg viewBox="0 0 24 24" aria-hidden="true"><path fill="var(--red)" d="M6.6 10.8a15.1 15.1 0 0 0 6.6 6.6l2.2-2.2a1 1 0 0 1 1-.25 11.4 11.4 0 0 0 3.6.57 1 1 0 0 1 1 1V20a1 1 0 0 1-1 1A17 17 0 0 1 3 4a1 1 0 0 1 1-1h3.5a1 1 0 0 1 1 1c0 1.25.2 2.45.57 3.57a1 1 0 0 1-.25 1z"/></svg>
      <span>712.555.0148</span>
    </li>
    <li class="contact-item">
      <svg viewBox="0 0 24 24" aria-hidden="true"><path fill="var(--red)" d="M2 5h20v14H2z"/><path fill="none" stroke="var(--card-white)" stroke-width="1.8" d="M2.5 5.5 12 13l9.5-7.5"/></svg>
      <span>hvacbrindle@mailbox.com</span>
    </li>
  </ul>

  <div class="back-brand">
    <div class="brand-dot" aria-hidden="true"></div>
    <span class="brand-word">Brindle's</span>
  </div>

  <p class="band-label bottom">FAMILY OWNED &amp; OPERATED</p>
</section>

</body>
</html>
```